Sales Brochure

We are looking for an 8.5 x 11 folding brochure in a landscape orientation that advertises our product and service offerings. This brochure should have content on both sides.

This brochure would be left at prospect client's business, so it needs to be fresh, professional, and focused.

We have attached two 1-page inserts that we would like you to use for inspiration for the written content in the brochure. We would like the main theme of the brochure to focus on professional, repeatable, and quality IT support for business.

The brochure should have the prospective clients email or call (will provide number and email to winner) to get additional information.

Please be creative with both the content and the design.

Went on vacation/holiday

```html
<!DOCTYPE html>
<html lang="en">
<head>
<meta charset="utf-8">
<title>Norvanta IT Services Brochure</title>
<link href="https://fonts.googleapis.com/css2?family=Montserrat:wght@500;600;700&family=Open+Sans:wght@400;600&display=swap" rel="stylesheet">
<style>
:root{
  --backdrop:#d3d3d3;
  --paper:#ebecee;
  --blue:#1d8fd8;
  --blue-deep:#136fb5;
  --ink:#2f3438;
  --muted:#5a6066;
  --white:#ffffff;
}
*{margin:0;padding:0;box-sizing:border-box}
html,body{width:800px;height:1200px;overflow:hidden;background:var(--backdrop)}
body{position:relative;font-family:"Open Sans",Arial,sans-serif;color:var(--ink)}
.spread{position:absolute;width:646px;height:500px;background:var(--paper);box-shadow:0 2px 8px rgba(0,0,0,.18)}
.spread--outside{left:71px;top:71px}
.spread--inside{left:83px;top:622px}
.spread svg.art{position:absolute;left:0;top:0;width:646px;height:500px}
.fold{position:absolute;top:0;width:22px;height:500px;background:linear-gradient(90deg,rgba(0,0,0,.16),rgba(0,0,0,0))}
.abs{position:absolute}
.brand{font-family:"Montserrat",sans-serif;font-weight:700;color:var(--blue);letter-spacing:1px}
.contact{font-family:"Montserrat",sans-serif;font-weight:600;font-size:8.5px;letter-spacing:.8px;color:var(--ink)}
.fine{font-size:4.8px;line-height:6px;color:var(--muted);text-align:justify}
.fine--white{color:var(--white);letter-spacing:.5px}
.tagline{font-family:"Montserrat",sans-serif;font-weight:600;font-size:13px;letter-spacing:2.3px;color:var(--blue)}
.url{font-family:"Montserrat",sans-serif;font-weight:500;font-size:10px;letter-spacing:2.2px;color:var(--white)}
.feature{width:70px;text-align:center}
.feature svg{width:14px;height:14px;display:block;margin:0 auto 4px}
.feature span{font-family:"Montserrat",sans-serif;font-size:4.6px;font-weight:600;color:var(--ink);letter-spacing:.3px}
.screen-name{font-family:"Montserrat",sans-serif;font-weight:700;font-size:15px;color:var(--white);letter-spacing:1px;text-align:center}
.section-title{font-family:"Montserrat",sans-serif;font-weight:700;font-size:12px;letter-spacing:2px;color:var(--blue)}
.item{position:absolute;display:flex;gap:9px}
.item .bullet{flex:none;width:17px;height:17px}
.item h3{font-family:"Montserrat",sans-serif;font-weight:600;font-size:7.5px;letter-spacing:1px;color:var(--blue);margin:2px 0 4px}
.item p{font-size:4.8px;line-height:6px;color:var(--muted);text-align:justify}
.closing{font-size:6.4px;line-height:8px;color:var(--blue);text-align:justify}
.plans-title{font-family:"Montserrat",sans-serif;font-weight:700;font-size:12px;line-height:15px;letter-spacing:2px;color:var(--blue-deep)}
.plans-title sup{font-size:7px}
.footer-contact{font-family:"Montserrat",sans-serif;font-weight:600;font-size:8px;letter-spacing:1.2px;color:var(--blue-deep)}
</style>
</head>
<body>

<!-- Outside spread: back panel + cover -->
<section class="spread spread--outside">
  <svg class="art" viewBox="0 0 646 500" aria-hidden="false">
    <defs>
      <radialGradient id="networkGlow" cx="50%" cy="55%" r="70%">
        <stop offset="0" stop-color="#7cc4ff"/>
        <stop offset=".35" stop-color="#1f5fae"/>
        <stop offset="1" stop-color="#0a1630"/>
      </radialGradient>
      <linearGradient id="officeLight" x1="0" y1="0" x2="1" y2="1">
        <stop offset="0" stop-color="#f6f8fa"/>
        <stop offset=".6" stop-color="#dfe5ea"/>
        <stop offset="1" stop-color="#c9cfd5"/>
      </linearGradient>
    </defs>
    <g role="img" aria-label="Glowing network of computers circling a globe">
      <path d="M0 0 H323 V262 C250 318 130 318 0 238 Z" fill="url(#networkGlow)"/>
    </g>
    <path d="M0 240 C120 330 250 326 323 266 L323 282 C250 345 110 340 0 258 Z" fill="var(--blue)"/>
    <path d="M0 420 C110 452 230 444 323 408 V500 H0 Z" fill="var(--blue)"/>
    <g role="img" aria-label="Businesswoman working on a laptop in a bright office">
      <path d="M323 0 H646 V250 C560 322 420 330 323 232 Z" fill="url(#officeLight)"/>
    </g>
    <path d="M323 238 C400 330 560 345 646 282 V300 C560 365 400 355 323 262 Z" fill="var(--blue)"/>
    <path d="M323 440 C420 418 560 462 646 418 V500 H323 Z" fill="var(--blue)"/>
    <g role="img" aria-label="Desktop monitor on a stand">
      <rect x="472" y="209" width="160" height="110" rx="3" fill="#2b2b2b"/>
      <rect x="477" y="214" width="150" height="92" fill="var(--blue)"/>
      <rect x="472" y="306" width="160" height="13" fill="#dcdfe2"/>
      <rect x="540" y="319" width="24" height="18" fill="#c3c7cb"/>
      <rect x="528" y="337" width="48" height="4" rx="2" fill="#b9bdc1"/>
    </g>
  </svg>
  <div class="fold" style="left:323px"></div>

  <div class="abs brand" style="left:0;width:323px;top:355px;text-align:center;font-size:18px">NORVANTA</div>
  <div class="abs contact" style="left:0;width:323px;top:387px;text-align:center">&#9743; 555-014-2288 &nbsp;www.norvanta.com</div>
  <div class="abs contact" style="left:0;width:323px;top:404px;text-align:center">88 Cedar Lane Box 210, Pine Ridge, AB</div>
  <p class="abs fine fine--white" style="left:34px;top:472px;width:260px">With over 30 years of industry experience, our highly skilled team is dedicated to providing you with the right expert at the right price.</p>

  <div class="abs brand" style="left:340px;top:24px;font-size:24px">NORVANTA</div>
  <div class="abs screen-name" style="left:477px;top:251px;width:150px">NORVANTA</div>
  <div class="abs tagline" style="left:323px;width:323px;top:380px;text-align:center">We take care of your IT needs</div>

  <div class="abs feature" style="left:370px;top:411px">
    <svg viewBox="0 0 14 14"><path d="M1 3 H5 L6.5 4.5 H13 V12 H1 Z" fill="none" stroke="var(--blue)" stroke-width="1.2"/></svg>
    <span>Infrastructure</span>
  </div>
  <div class="abs feature" style="left:433px;top:411px">
    <svg viewBox="0 0 14 14"><path d="M3.5 11 A3 3 0 0 1 3.5 5 A4 4 0 0 1 11 6 A2.5 2.5 0 0 1 11 11 Z" fill="var(--blue)"/><path d="M7 10 V6.5 M5.5 8 L7 6.5 L8.5 8" stroke="#fff" stroke-width="1" fill="none"/></svg>
    <span>Cloud Integration</span>
  </div>
  <div class="abs feature" style="left:497px;top:411px">
    <svg viewBox="0 0 14 14"><rect x="1.5" y="4" width="11" height="7" rx="1.5" fill="none" stroke="var(--blue)" stroke-width="1.2"/><path d="M1.5 8 H12.5" stroke="var(--blue)" stroke-width="1"/></svg>
    <span>Desktop Support</span>
  </div>
  <div class="abs feature" style="left:558px;top:411px">
    <svg viewBox="0 0 14 14"><g fill="var(--blue)"><rect x="1" y="10" width="2" height="3"/><rect x="4" y="8" width="2" height="5"/><rect x="7" y="5" width="2" height="8"/><rect x="10" y="1" width="2" height="12"/></g></svg>
    <span>Data Protection</span>
  </div>
  <div class="abs url" style="left:323px;width:323px;top:474px;text-align:center">www.norvanta.com</div>
</section>

<!-- Inside spread: services + service plans -->
<section class="spread spread--inside">
  <svg class="art" viewBox="0 0 646 500">
    <defs>
      <linearGradient id="deskLight" x1="0" y1="0" x2="1" y2="1">
        <stop offset="0" stop-color="#f4f6f7"/>
        <stop offset="1" stop-color="#c7ccd1"/>
      </linearGradient>
      <symbol id="chevronBullet" viewBox="0 0 17 17">
        <circle cx="8.5" cy="8.5" r="8" fill="#dfe3e7"/>
        <path d="M5 5 L8.5 8.5 L5 12 M8.5 5 L12 8.5 L8.5 12" fill="none" stroke="var(--blue)" stroke-width="1.6"/>
      </symbol>
    </defs>
    <g role="img" aria-label="Hands typing on a laptop at a desk">
      <path d="M0 500 V432 C100 362 240 352 323 392 V500 Z" fill="url(#deskLight)"/>
    </g>
    <path d="M0 416 C100 336 250 330 323 372 V392 C240 352 100 362 0 432 Z" fill="var(--blue)"/>
    <g role="img" aria-label="Hands working on a laptop and mouse">
      <path d="M338 0 C362 100 520 162 646 68 V0 Z" fill="url(#deskLight)"/>
    </g>
    <path d="M322 0 C350 118 520 182 646 84 V68 C520 162 362 100 338 0 Z" fill="var(--blue)"/>
    <path d="M326 0 C360 140 540 198 646 100 V94 C540 190 362 134 332 0 Z" fill="var(--blue-deep)"/>
    <g role="img" aria-label="Desktop monitor on a stand">
      <rect x="493" y="107" width="116" height="84" rx="3" fill="#2b2b2b"/>
      <rect x="497" y="111" width="108" height="68" fill="var(--blue)"/>
      <rect x="493" y="179" width="116" height="12" fill="#dcdfe2"/>
      <rect x="542" y="191" width="18" height="12" fill="#c3c7cb"/>
      <rect x="532" y="203" width="38" height="3" rx="1.5" fill="#b9bdc1"/>
    </g>
  </svg>
  <div class="fold" style="left:322px"></div>

  <h2 class="abs section-title" style="left:18px;top:38px">NORVANTA SERVICES</h2>

  <div class="item" style="left:16px;top:74px;width:292px">
    <svg class="bullet"><use href="#chevronBullet"/></svg>
    <div><h3>DESKTOP SUPPORT</h3><p>Our desktop support technicians are available around the clock to respond to support calls or incidents logged in our efficient online ticketing system. Technicians respond initially by using remote support, but when the situation requires it, a technician comes on-site. Regular face-to-face IT check-ups and satisfaction surveys ensure you are pleased with the quality of the desktop support you are receiving.</p></div>
  </div>
  <div class="item" style="left:16px;top:131px;width:292px">
    <svg class="bullet"><use href="#chevronBullet"/></svg>
    <div><h3>SYSTEMS MANAGEMENT</h3><p>We make our expertise in system and network technologies (such as email, servers, cloud, wireless, printing and remote access) work for you.</p></div>
  </div>
  <div class="item" style="left:16px;top:178px;width:292px">
    <svg class="bullet"><use href="#chevronBullet"/></svg>
    <div><h3>DATA PROTECTION</h3><p>We offer cost effective solutions to make sure your information is backed up securely. We ensure that backups are run properly and consistently, and monitor those backups on a daily basis.</p></div>
  </div>
  <div class="item" style="left:16px;top:226px;width:292px">
    <svg class="bullet"><use href="#chevronBullet"/></svg>
    <div><h3>IT PROJECTS</h3><p>We plan, manage and implement all your technology projects. We promise to meet your stated objectives, on time and on budget.</p></div>
  </div>
  <p class="abs closing" style="left:18px;top:282px;width:290px">We pride ourselves in delivering services that increase your productivity, helping your business run more efficiently and effectively. We are your IT department.</p>

  <h2 class="abs plans-title" style="left:336px;top:212px">STEADYCARE<sup>TM</sup><br>SERVICE PLANS</h2>
  <p class="abs fine" style="left:336px;top:248px;width:290px">Keeping your technology safe and up-to-date is not a one-time job. Our SteadyCARE service plans deliver peace of mind for all your technology data and infrastructure at an affordable price. Knowing your computers are safe and maintained saves you stress, letting you focus on what you do best. We offer plans that secure your workstation, optimize your servers and network, and keep your data safe.</p>

  <div class="item" style="left:334px;top:290px;width:294px">
    <svg class="bullet"><use href="#chevronBullet"/></svg>
    <div><h3>STEADYCARE&trade; WORKSTATION</h3><p>We provide responsive, quality IT solutions to Pine Ridge and the surrounding towns. Our unique SteadyCARE service plans provide fast response times, and our project services provide expert IT help at an affordable price. Professionalism and reliable customer service is our standard.</p></div>
  </div>
  <div class="item" style="left:334px;top:348px;width:294px">
    <svg class="bullet"><use href="#chevronBullet"/></svg>
    <div><h3>STEADYCARE&trade; INFRASTRUCTURE</h3><p>Our SteadyCARE Infrastructure solution ensures that your servers and other vital network devices run at peak performance. This includes being proactive about general maintenance tasks, monitoring and alerting. Because we know your IT environment, we are quickly able to handle any issues that occur, considerably speeding up recovery times.</p></div>
  </div>
  <div class="item" style="left:334px;top:406px;width:294px">
    <svg class="bullet"><use href="#chevronBullet"/></svg>
    <div><h3>STEADYCARE&trade; DATA PROTECTION</h3><p>When was the last time you ran a full backup of your data, and then tested the data to make sure it retrieves properly? SteadyCARE Data Protection means we monitor your backups on a daily basis. Problematic backups are brought to our attention, and we determine the cause of the problem and make adjustments so the next backup runs successfully. We also perform file integrity checks to confirm that the backups are valid, and periodically conduct test file restores.</p></div>
  </div>

  <div class="abs footer-contact" style="left:356px;top:479px">&#9743; 555-014-2288</div>
  <div class="abs footer-contact" style="left:530px;top:479px">www.norvanta.com</div>
</section>

</body>
</html>
```